Remote Computer Support PostCard

We need a Postcard Ad for marketing to businesses that need Remote Computer Support and Security. 2 sided and able to be mailed. Can be any color but color we use mostly is red. Remote Computer Support and Security per PC. Includes Remote Monitoring and Maintenance(RMM) Agent, Business Security Tools including Antivirus, Anti Malware, Ransomware Protection, Intrusion Prevention, Content Filtering and others. All remote support you need for $69.99 per pc per month.

Target Market(s)

All Businesses

Industry/Entity Type

Computer Support for Businesses

Colors
EB3D1F
EC4F4E
F09395
F8D3D4
FCEDEE

Requirements
Must have
• BrivoLane, Inc. (555) 246-9137 . Sales@brivolane.example. Designed to be mailed. 6x9 Postcard Mailer Size Final 6.25" x 9" Ink & Bleed Four Color Process, Full Bleed Two Sides. Must have places for postage.
Nice to have
• Main lines should be in top 1/3 of postcard to stand out in mail.

```html
<!DOCTYPE html>
<html lang="en">
<head>
<meta charset="utf-8">
<title>BrivoLane Remote Support Postcard</title>
<link rel="stylesheet" href="https://fonts.googleapis.com/css2?family=Montserrat:wght@500;600;700;800&family=Quicksand:wght@400;500&display=swap">
<style>
  :root {
    --ink: #141414;
    --paper: #ffffff;
    --brand-red: #d7232a;
    --accent-yellow: #f8e21a;
    --text-light: #f4eeee;
    --photo-dark: #1a0606;
    --photo-mid: #4a1512;
    --photo-warm: #6d2a22;
  }
  * { margin: 0; padding: 0; box-sizing: border-box; }
  html, body { width: 1200px; height: 811px; overflow: hidden; background: var(--paper); }
  .postcard { position: relative; width: 1200px; height: 811px; background: var(--paper); overflow: hidden; }

  .hero-photo {
    position: absolute; left: 0; top: 0; width: 1200px; height: 600px;
    background:
      radial-gradient(ellipse 300px 220px at 600px 370px, rgba(170,60,55,.55), transparent 70%),
      radial-gradient(ellipse 420px 260px at 600px 120px, rgba(120,70,65,.45), transparent 75%),
      linear-gradient(160deg, var(--photo-warm) 0%, var(--photo-mid) 40%, var(--photo-dark) 100%);
  }
  .hero-shade {
    position: absolute; left: 0; top: 0; width: 1200px; height: 600px;
    background: linear-gradient(90deg, rgba(10,0,0,.55) 0%, rgba(10,0,0,0) 35%, rgba(10,0,0,0) 65%, rgba(10,0,0,.5) 100%);
  }
  .red-band { position: absolute; left: 0; top: 600px; width: 1200px; height: 13px; background: var(--brand-red); }

  .kicker {
    position: absolute; left: 0; width: 1200px; top: 64px; text-align: center;
    font-family: "Quicksand", sans-serif; font-weight: 500; font-size: 32px;
    color: var(--accent-yellow); letter-spacing: .5px;
  }
  .headline {
    position: absolute; left: 0; width: 1200px; top: 102px; text-align: center;
    font-family: "Montserrat", sans-serif; font-weight: 700; font-size: 52px;
    color: var(--paper);
  }

  .offer {
    position: absolute; left: 78px; top: 188px; width: 230px;
    transform: rotate(-4deg); transform-origin: left top;
    font-family: "Montserrat", sans-serif; color: var(--paper); text-align: center;
  }
  .offer-lead { font-size: 16px; font-weight: 600; letter-spacing: .4px; }
  .offer-price { font-size: 58px; font-weight: 800; color: var(--accent-yellow); line-height: 1.05; }
  .offer-then { font-size: 22px; font-weight: 600; margin-top: 4px; white-space: nowrap; }
  .offer-unit { font-size: 14px; font-weight: 600; margin-top: 2px; }

  .feature-list {
    position: absolute; list-style: none;
    font-family: "Quicksand", sans-serif; font-weight: 500; font-size: 17.5px;
    color: var(--text-light); line-height: 27px;
  }
  .feature-list li { position: relative; padding-left: 25px; }
  .feature-list li.bullet::before {
    content: ""; position: absolute; left: 0; top: 8px; width: 10px; height: 10px;
    border: 2px solid var(--accent-yellow);
  }
  .features-left { left: 48px; top: 377px; }
  .features-right { left: 864px; top: 379px; }

  .contact-tag {
    position: absolute; left: 0; top: 635px; width: 276px; height: 41px;
    background: var(--brand-red); border-radius: 0 21px 21px 0;
    font-family: "Montserrat", sans-serif; font-weight: 700; font-size: 26px;
    color: var(--paper); line-height: 41px; padding-left: 53px;
  }
  .contact-phone {
    position: absolute; left: 46px; top: 688px;
    font-family: "Montserrat", sans-serif; font-weight: 700; font-size: 43px; color: var(--ink);
  }
  .contact-email {
    position: absolute; left: 57px; top: 744px;
    font-family: "Montserrat", sans-serif; font-weight: 500; font-size: 28px; color: var(--ink);
  }

  .brand-name {
    position: absolute; left: 830px; top: 684px;
    display: flex; align-items: center; gap: 12px;
    font-family: "Montserrat", sans-serif; font-weight: 700; font-size: 44px; color: var(--ink);
  }
  .brand-mark { width: 22px; height: 22px; background: var(--brand-red); }
</style>
</head>
<body>
<main class="postcard">
  <div class="hero-photo" role="img" aria-label="Photo of hands holding a tablet showing a glowing antivirus chip, on a dark wooden desk with a keyboard, in deep red tones"></div>
  <div class="hero-shade"></div>
  <div class="red-band"></div>

  <p class="kicker">Finaly Computer Security and</p>
  <h1 class="headline">Support Made Easy!</h1>

  <div class="offer">
    <p class="offer-lead">ONE TIME SETUP FEE OF</p>
    <p class="offer-price">$69.99</p>
    <p class="offer-then">THEN ONLY $69.99</p>
    <p class="offer-unit">PER MONTH PER PC</p>
  </div>

  <ul class="feature-list features-left">
    <li class="bullet">Automated OS Updates</li>
    <li class="bullet">Automated System Cleanup</li>
    <li class="bullet">Managed Antivirus</li>
    <li class="bullet">Including Ransomware</li>
    <li>Detection and Protection</li>
    <li class="bullet">Monthly Reports</li>
  </ul>

  <ul class="feature-list features-right">
    <li class="bullet">Automated Remote Support</li>
    <li class="bullet">Remote Monitoring and</li>
    <li>Maintenance Tools</li>
    <li class="bullet">Monitor Your Devices in Real-time.</li>
    <li class="bullet">Instantly Informing you of</li>
    <li>Current Issues and</li>
    <li class="bullet">Flagging Potential Problems.</li>
  </ul>

  <div class="contact-tag">KEEP IN TOUCH</div>
  <p class="contact-phone">(555) 246-9137</p>
  <p class="contact-email">Sales@brivolane.example</p>

  <div class="brand-name"><span class="brand-mark"></span>BrivoLane</div>
</main>
</body>
</html>
```